New Baby Formula Company Needs a Shopify Website Design

We are launching a baby formula company and need a Shopify website design. We have a patented product that is a disposable pouch with a frangible seal through the middle. The top half contains formula powder and the bottom half contains purified water. There is also a bottle nipple on the corner under the cap in order to feed the baby. You just need to squeeze the bottom half of the pouch to break the seal and then the water and formula will mix. You then only need to shake it and then remove the cap and feed the baby. We will also sell formula in containers like the other formula companies. We want this website to stand out and look professional. We don't want a boring layout, but something unique and captivating. I have attached a mockup rendering of our product, though it's not the finished product and our logo. This will let you know the color scheme we are going for. Let me know if you have any further questions. Thank you

```html
<!DOCTYPE html>
<html lang="en">
<head>
<meta charset="utf-8">
<title>Nuvo Baby – Baby Formula</title>
<link href="https://fonts.googleapis.com/css2?family=Roboto:wght@400;500;700&family=Lato:wght@400;700&family=Rubik:wght@400;500&family=Great+Vibes&display=swap" rel="stylesheet">
<style>
:root{
  --olive:#adb944;
  --olive-dark:#98a534;
  --lime-soft:#e9f1a8;
  --ink:#111;
  --text:#333;
  --muted:#555;
  --hero-bg:#eeeef0;
  --footer:#0c0c0c;
  --star:#f2b705;
}
*{box-sizing:border-box;margin:0;padding:0}
html,body{width:1200px;height:3596px;overflow:hidden;background:#fff}
body{font-family:'Roboto',sans-serif;color:var(--text)}
.page{position:relative;width:1200px;height:3596px;overflow:hidden}
.abs{position:absolute}
.btn{position:absolute;display:flex;align-items:center;justify-content:center;background:var(--olive);color:#111;font:500 15px 'Roboto',sans-serif;border-radius:22px;text-transform:uppercase}
.placeholder{position:absolute}

/* top bar */
.topbar{position:absolute;left:0;top:0;width:1200px;height:42px;background:var(--olive);color:#222;font-size:15px}
.topbar svg{position:absolute;left:0;top:40px}
/* hero */
.hero{position:absolute;left:0;top:0;width:1200px;height:610px;background:var(--hero-bg)}
.hero-photo{position:absolute;left:640px;top:42px;width:560px;height:568px;background:radial-gradient(ellipse at 60% 45%,#e9c3a8 0%,#ddb39a 35%,#ecebec 70%,#f2f2f3 100%)}
.search{position:absolute;left:377px;top:67px;width:418px;height:41px;border:1px solid #bbb;border-radius:21px;background:#f6f6f7;font-size:15px;padding:11px 18px;color:#333}
.search svg{position:absolute;right:16px;top:12px}
.account{position:absolute;left:935px;top:64px;width:163px;height:45px;background:#fff;border:1px solid #e3e3e3;font-size:12px;color:var(--olive-dark)}
.nav{position:absolute;top:137px;font-size:15px;color:#111;font-weight:500}
.nav.active{color:var(--olive)}
.arrow-btn{position:absolute;width:38px;height:38px;border:1.5px solid #222;border-radius:50%}
.arrow-btn svg{position:absolute;left:11px;top:11px}
.welcome{left:112px;top:236px;font:52px 'Great Vibes',cursive;color:#222}
.brand-big{left:110px;top:292px;font:400 86px 'Lato',sans-serif;color:#111;line-height:1}
.brand-sub{left:112px;top:384px;font:400 38px 'Lato',sans-serif;color:#111}

/* about */
.about-img{left:63px;top:690px;width:551px;height:513px;border-radius:48% 52% 40% 60%/55% 50% 50% 45%;background:radial-gradient(circle at 30% 35%,#e6ef9c 0,#e9f1a8 40%,#f3f6d9 70%,#fff 100%)}
.eyebrow{font:500 15px 'Roboto',sans-serif;color:#111}
.h2{font:400 27px/39px 'Roboto',sans-serif;color:#111}
.para{font:400 15px/27.5px 'Roboto',sans-serif;color:#444}
.feat{font:400 20px 'Rubik',sans-serif;color:#111;display:flex;align-items:center;gap:10px}
.feat::before{content:"";width:12px;height:12px;border-radius:50%;background:var(--olive)}
.section-title{font:400 40px 'Lato',sans-serif;color:#111;text-align:center}

/* directions */
.dir-title{left:112px;top:1268px;font:700 36px 'Lato',sans-serif;color:#111}
.dir-desc{left:112px;top:1328px;width:310px;font:400 15px/24px 'Roboto',sans-serif;color:#333}
.countdown{position:absolute;top:1388px;text-align:center;width:70px}
.countdown b{display:block;font:500 36px 'Roboto',sans-serif;color:#111}
.countdown span{display:block;font:400 20px 'Roboto',sans-serif;color:#666;margin-top:4px}

/* products */
.product{position:absolute;top:1800px;width:240px;text-align:center}
.product .pimg{width:120px;height:150px;margin:0 auto;border-radius:10px}
.product .ptitle{margin-top:22px;font-size:16px;color:#333}
.product .price{margin-top:8px;font:500 15px 'Roboto',sans-serif;color:#111}
.product .price s{color:#555;font-weight:400;margin-left:10px}
.product .stars{margin-top:4px;font-size:11px;color:var(--star);letter-spacing:3px}

/* updates */
.card{position:absolute;top:2624px;width:306px}
.card .cimg{height:246px;border-radius:14px}
.card h3{margin-top:26px;font:500 20px 'Roboto',sans-serif;color:#111}
.card p{margin-top:10px;font:400 15px/25px 'Roboto',sans-serif;color:#444}

/* footer */
.footer{position:absolute;left:0;top:3066px;width:1200px;height:530px;background:var(--footer);color:#fff}
.f-logo{position:absolute;left:112px;top:52px;width:104px;height:102px;border:2px solid #fff;border-radius:50%;display:flex;align-items:center;justify-content:center;font:500 19px 'Roboto',sans-serif}
.f-sub{position:absolute;left:328px;top:50px;font:500 38px/44px 'Rubik',sans-serif}
.f-email{position:absolute;left:582px;top:74px;width:374px;height:42px;background:#fff;border-radius:21px;color:#888;font-size:14px;padding:13px 14px}
.f-btn{position:absolute;left:974px;top:77px;width:114px;height:36px;background:#fff;color:#111;border-radius:18px;font:500 15px 'Roboto',sans-serif;display:flex;align-items:center;justify-content:center}
.f-head{position:absolute;top:202px;font:500 21px 'Roboto',sans-serif}
.f-links{position:absolute;top:249px;font-size:15px;line-height:36.8px;list-style:none}
.f-contact{position:absolute;left:146px;font-size:15px;line-height:22px}
.f-contact b{font-weight:700}
.f-icon{position:absolute;left:114px}
.copy{position:absolute;left:114px;top:470px;font-size:15px}
.pay{position:absolute;top:471px;width:30px;height:19px;border-radius:3px;background:#fff}
</style>
</head>
<body>
<div class="page">

  <!-- Hero -->
  <section class="hero">
    <div class="hero-photo" role="img" aria-label="Smiling baby wrapped in a white hooded towel"></div>
    <div class="search">Search
      <svg width="16" height="16" viewBox="0 0 16 16"><circle cx="6.5" cy="6.5" r="5" fill="none" stroke="#111" stroke-width="2"/><line x1="10.3" y1="10.3" x2="15" y2="15" stroke="#111" stroke-width="2.2"/></svg>
    </div>
    <div class="account">
      <svg class="abs" style="left:6px;top:11px" width="22" height="22" viewBox="0 0 22 22"><circle cx="11" cy="7" r="5" fill="none" stroke="#333" stroke-width="1.5"/><path d="M2 21c1-5 5-7 9-7s8 2 9 7" fill="none" stroke="#333" stroke-width="1.5"/></svg>
      <div class="abs" style="left:32px;top:8px;line-height:14px">Account<br>Log in</div>
      <svg class="abs" style="left:94px;top:10px" width="26" height="24" viewBox="0 0 26 24"><path d="M3 9h20l-2 12H5z" fill="none" stroke="#333" stroke-width="1.5"/><path d="M8 9a5 5 0 0 1 10 0" fill="none" stroke="#333" stroke-width="1.5"/><circle cx="16" cy="6" r="5" fill="var(--olive)"/></svg>
      <div class="abs" style="left:124px;top:8px;line-height:14px">Total<br>$0.00</div>
    </div>
    <div class="nav active" style="left:335px">HOME</div>
    <div class="nav" style="left:410px">ABOUT US</div>
    <div class="nav" style="left:516px">PRODUCTS</div>
    <div class="nav" style="left:626px">TESTIMONIALS</div>
    <div class="nav" style="left:769px">CONTACT US</div>

    <div class="arrow-btn" style="left:33px;top:317px"><svg width="14" height="14" viewBox="0 0 14 14"><path d="M9 2L4 7l5 5" fill="none" stroke="#111" stroke-width="1.8"/></svg></div>
    <div class="arrow-btn" style="left:1142px;top:317px"><svg width="14" height="14" viewBox="0 0 14 14"><path d="M5 2l5 5-5 5" fill="none" stroke="#111" stroke-width="1.8"/></svg></div>

    <div class="abs welcome">Welcome To</div>
    <div class="abs brand-big">Nuvo Baby</div>
    <div class="abs brand-sub">Baby Formala</div>
    <div class="btn" style="left:112px;top:449px;width:122px;height:42px">Buy Now</div>
  </section>

  <header class="topbar">
    <div class="abs" style="left:112px;top:10px">Free shipping on all orders over $70</div>
    <div class="abs" style="left:852px;top:10px">Country/region ⌄</div>
    <div class="abs" style="left:1019px;top:10px">English ⌄</div>
    <svg width="1200" height="6" viewBox="0 0 1200 6" preserveAspectRatio="none"><path d="M0 0 L1200 0 L1200 2 Q1195 6 1190 2 Q1185 6 1180 2 Q1175 6 1170 2 Q1165 6 1160 2 Q1155 6 1150 2 Q1145 6 1140 2 Q1135 6 1130 2 Q1125 6 1120 2 Q1115 6 1110 2 Q1105 6 1100 2 Q1095 6 1090 2 Q1085 6 1080 2 Q1075 6 1070 2 Q1065 6 1060 2 Q1055 6 1050 2 Q1045 6 1040 2 Q1035 6 1030 2 Q1025 6 1020 2 Q1015 6 1010 2 Q1005 6 1000 2 L0 2 Z" fill="var(--olive)"/><rect x="0" y="0" width="1000" height="3" fill="var(--olive)"/></svg>
  </header>

  <!-- About -->
  <div class="placeholder about-img" role="img" aria-label="Baby sitting with a feeding bottle beside a formula pouch"></div>
  <div class="abs eyebrow" style="left:645px;top:718px">About Us</div>
  <h2 class="abs h2" style="left:645px;top:748px;width:470px">Lorem ipsum dolor sit amet, conseur adipiscing consectetur elit.</h2>
  <p class="abs para" style="left:645px;top:845px;width:455px">Lorem ipsum dolor sit amet, consectetur adipiscing elit, sed do eiusmod tempor incididunt ut labore et dolore magna aliqua. Ut enim ad minim veniam, quis nostrud exercitation ullamco laboris nisi ut aliquip ex ea commodo consequat. Duis aute irure dolor in reprehenderit in voluptate velit esse cillum dolore eu fugiat nulla pariatur. Excepteur sint occaecat cupidatat.</p>
  <div class="abs feat" style="left:643px;top:1035px">24/7 Support</div>
  <div class="abs feat" style="left:925px;top:1035px">24/7 Support</div>
  <div class="abs feat" style="left:643px;top:1080px">Quick Delivery</div>
  <div class="abs feat" style="left:925px;top:1080px">Quick Delivery</div>
  <div class="btn" style="left:643px;top:1141px;width:122px;height:41px">Read More</div>

  <!-- Directions -->
  <h2 class="abs dir-title">Directions For Use</h2>
  <p class="abs dir-desc">Consult Your Bany's Physican About The Appropriate Use Of Formula For Your Child.</p>
  <div class="abs feat" style="left:112px;top:1400px">Squeeze</div>
  <div class="abs feat" style="left:112px;top:1446px">Shake</div>
  <div class="abs feat" style="left:112px;top:1492px">Feed</div>
  <div class="placeholder" style="left:419px;top:1276px;width:397px;height:356px;border-radius:20px;background:linear-gradient(135deg,#f4f4f2 0%,#dfe5b6 45%,#9aa93e 100%)" role="img" aria-label="Formula can and two formula pouches"></div>
  <div class="abs" style="left:760px;top:1276px;width:330px;text-align:right;font:500 20px 'Roboto',sans-serif;color:#111">Hurry up limited-time offer</div>
  <div class="abs" style="left:760px;top:1320px;width:330px;text-align:right;font:400 15px/26px 'Roboto',sans-serif;color:#222">Infant Formula <span style="font-size:20px">Milk-Based</span><br><span style="font-size:20px">Powder</span> With Purified Water</div>
  <div class="countdown" style="left:894px"><b>10</b><span>Hour</span></div>
  <div class="countdown" style="left:962px"><b>37</b><span>Min</span></div>
  <div class="countdown" style="left:1034px"><b>50</b><span>Sec</span></div>
  <div class="btn" style="left:967px;top:1491px;width:123px;height:42px">Buy Now</div>

  <!-- Products -->
  <h2 class="abs section-title" style="left:0;top:1716px;width:1200px">Our Products</h2>
  <div class="product" style="left:91px">
    <div class="pimg" role="img" aria-label="Silver formula can" style="width:90px;border-radius:8px;background:linear-gradient(90deg,#bfbfbf,#f3f3f3,#a9a9a9)"></div>
    <div class="ptitle">Lorem ipsum dolor sit amet.</div>
    <div class="price">$29.00 <s>$33.00</s></div>
    <div class="stars">★★★★★</div>
  </div>
  <div class="product" style="left:349px">
    <div class="pimg" role="img" aria-label="Formula pouch front" style="background:linear-gradient(180deg,#f1f3e2 0%,#c6d06f 60%,#9aa93e 100%)"></div>
    <div class="ptitle">Lorem ipsum dolor sit amet.</div>
    <div class="price">$30.00 <s>$34.00</s></div>
    <div class="stars">★★★★★</div>
  </div>
  <svg class="abs" style="left:537px;top:1806px" width="16" height="52" viewBox="0 0 16 52"><path d="M1 2h3l2 9h8l1-6H5" fill="none" stroke="#555" stroke-width="1.3"/><circle cx="7" cy="13" r="1.2" fill="#555"/><circle cx="13" cy="13" r="1.2" fill="#555"/><path d="M8 32l-5-5a3 3 0 0 1 5-3 3 3 0 0 1 5 3z" fill="none" stroke="#555" stroke-width="1.3"/><ellipse cx="8" cy="45" rx="7" ry="4" fill="none" stroke="#555" stroke-width="1.3"/><circle cx="8" cy="45" r="1.6" fill="#555"/></svg>
  <div class="product" style="left:605px">
    <div class="pimg" role="img" aria-label="Formula pouch back" style="width:80px;background:linear-gradient(180deg,#eef0df 0%,#c6d06f 70%,#9aa93e 100%)"></div>
    <div class="ptitle">Lorem ipsum dolor sit amet.</div>
    <div class="price">$27.00 <s>$30.00</s></div>
    <div class="stars">★★★★★</div>
  </div>
  <div class="product" style="left:862px">
    <div class="pimg" role="img" aria-label="White formula can with green label" style="width:94px;height:126px;margin-top:4px;background:linear-gradient(90deg,#d9d9d9,#fbfbf6,#cfcfcf)"></div>
    <div class="ptitle" style="margin-top:42px">Lorem ipsum dolor sit amet.</div>
    <div class="price">$29.00 <s>$36.00</s></div>
    <div class="stars">★★★★★</div>
  </div>

  <!-- Feature -->
  <div class="placeholder" style="left:146px;top:2148px;width:377px;height:272px;border-radius:20px;background:linear-gradient(90deg,#c0cb62 0%,#eadfcf 45%,#f2d9c6 55%,#c0cb62 100%)" role="img" aria-label="Baby sitting among formula pouches and cans"></div>
  <div class="abs eyebrow" style="left:603px;top:2132px">Lorem ipsum dolor sit amet</div>
  <h2 class="abs" style="left:600px;top:2164px;width:500px;font:400 32px/40px 'Roboto',sans-serif;color:#111">Lorem ipsum dolor sit amet, cing elit, sed do magna aliqua.</h2>
  <p class="abs para" style="left:603px;top:2257px;width:490px;font-size:15px;line-height:28.5px">Lorem ipsum dolor sit amet, consectetur adipiscing elit, sed do eiusod tempor incididunt ut labore et dolore magna aliqua. Quis ipsum uesse ultrices gravida. Risus commodo viverra maecenas accumsan lacus vel facilisis ut labore et dolore magna aliqua.</p>
  <div class="btn" style="left:600px;top:2383px;width:122px;height:41px">Buy Now</div>

  <!-- Recent updates -->
  <h2 class="abs section-title" style="left:0;top:2516px;width:1250px">Our Recent Updates</h2>
  <article class="card" style="left:112px">
    <div class="cimg" role="img" aria-label="Parent feeding a baby with a bottle" style="background:linear-gradient(135deg,#7a7a9a,#c9a48f 55%,#e8dfe0)"></div>
    <h3>Lorem ipsum dolor sit amet.</h3>
    <p>Lorem ipsum dolor sit amet, consectetur adipiscing elit,Quis ultrices gravida...</p>
  </article>
  <article class="card" style="left:446px">
    <div class="cimg" role="img" aria-label="Mother holding a laughing baby" style="background:linear-gradient(135deg,#e8e4df,#d9b59c 55%,#f0ece8)"></div>
    <h3>Lorem ipsum dolor sit amet.</h3>
    <p>Lorem ipsum dolor sit amet, consectetur adipiscing elit,Quis ultrices gravida...</p>
  </article>
  <article class="card" style="left:781px">
    <div class="cimg" role="img" aria-label="Father bottle-feeding a baby" style="background:linear-gradient(135deg,#3a2a24,#b98a6f 55%,#f1f1f1)"></div>
    <h3>Lorem ipsum dolor sit amet.</h3>
    <p>Lorem ipsum dolor sit amet, consectetur adipiscing elit,Quis ultrices gravida...</p>
  </article>

  <!-- Footer -->
  <footer class="footer">
    <div class="f-logo">NuvoBaby</div>
    <div class="f-sub">Subscribe To<br>Newsletter</div>
    <div class="f-email">Email</div>
    <div class="f-btn">SUBSCRIBE</div>

    <div class="f-head" style="left:112px">Contact Info</div>
    <div class="f-head" style="left:466px">Quick Links</div>
    <div class="f-head" style="left:675px">Customer Service</div>
    <div class="f-head" style="left:943px">Help Links</div>

    <ul class="f-links" style="left:473px"><li>Home</li><li>About Us</li><li>Products</li><li>Testimonials</li><li>Contact Us</li></ul>
    <ul class="f-links" style="left:681px"><li>Customer Service</li><li>Home</li><li>Product</li><li>Collections</li><li>Blog</li></ul>
    <ul class="f-links" style="left:944px"><li>About us</li><li>Contact us</li><li>Faq</li><li>Privacy policy</li><li>Return and exchange</li></ul>

    <svg class="f-icon" style="top:273px" width="20" height="16" viewBox="0 0 20 16"><rect x="0" y="0" width="20" height="16" rx="2" fill="#fff"/><path d="M1 2l9 7 9-7" fill="none" stroke="#0c0c0c" stroke-width="1.6"/></svg>
    <div class="f-contact" style="top:249px"><b>Email:</b><br>info@nuvobaby.com</div>
    <svg class="f-icon" style="top:336px" width="18" height="18" viewBox="0 0 18 18"><path d="M4 1l3 4-2 2c1 2 4 5 6 6l2-2 4 3-2 3C8 17 1 10 1 4z" fill="#fff"/></svg>
    <div class="f-contact" style="top:312px"><b>Phone No:</b><br>+1(555) 014 2290</div>
    <svg class="f-icon" style="top:393px;left:116px" width="14" height="20" viewBox="0 0 14 20"><path d="M7 0a7 7 0 0 1 7 7c0 5-7 13-7 13S0 12 0 7a7 7 0 0 1 7-7z" fill="#fff"/><circle cx="7" cy="7" r="2.6" fill="#0c0c0c"/></svg>
    <div class="f-contact" style="top:373px"><b>Location</b><br>NuvoBaby Baby Formula,USA</div>

    <div class="copy">Copyright © 2024 NuvoBaby all rights reserved.</div>
    <div class="pay" style="left:854px"></div>
    <div class="pay" style="left:894px"></div>
    <div class="pay" style="left:935px"></div>
    <div class="pay" style="left:976px"></div>
    <div class="pay" style="left:1017px"></div>
    <div class="pay" style="left:1058px"></div>
  </footer>
</div>
</body>
</html>
```